Real Estate Business Cards

Looking for a clean, sharp and professional look for our Real Estate investment Fund that invests in Multi Family Apartment buildings.

Target Market(s)

Real Estate Fund

Industry/Entity Type

Real Estate

Contact Information for Business Card

Company Description: Real Estate Investment Fund
Company Name: RKW Holdings
Name: Marcus Olvane
Cell: (917) 482-0657
Email: marcus@rkwholdings-example.com
Website: www.rkwholdings-example.com
Address: 418, 9th Street, Brooklyn NY 11218

Colors

Designer to choose colors to be used in the design.

Requirements
Nice to have
• Colors to match logo

```html
<!DOCTYPE html>
<html lang="en">
<head>
<meta charset="utf-8">
<title>RKW Holdings – Business Card</title>
<link href="https://fonts.googleapis.com/css2?family=Cinzel:wght@500;600&family=Roboto:wght@400&display=swap" rel="stylesheet">
<style>
  :root {
    --backdrop: #a0a0a0;
    --brand-blue: #0e71a8;
    --card-light: #f4f4f4;
    --ink: #3a3a3a;
    --ink-dark: #444444;
    --white: #f2f2f2;
  }
  * { margin: 0; padding: 0; box-sizing: border-box; }
  html, body { width: 1200px; height: 1080px; overflow: hidden; }
  body { background: var(--backdrop); position: relative; font-family: "Roboto", Arial, sans-serif; }

  .card { position: absolute; left: 232px; width: 734px; height: 405px; border-radius: 24px; overflow: hidden; }
  .card-front { top: 92px; background: var(--brand-blue); }
  .card-back { top: 538px; background: var(--card-light); }

  .front-name {
    position: absolute; left: 0; right: 0; top: 325px;
    text-align: center; color: var(--white);
    font-family: "Cinzel", "Times New Roman", serif; font-weight: 500;
    font-size: 52px; letter-spacing: 1px; line-height: 1;
  }
  .front-mark {
    position: absolute; left: 317px; top: 150px; width: 100px; height: 100px;
    border: 6px solid var(--white); border-radius: 4px;
  }

  .back-brand {
    position: absolute; left: 34px; top: 52px; display: flex; align-items: center; gap: 14px;
  }
  .back-brand .mark { width: 44px; height: 44px; background: var(--brand-blue); }
  .back-brand .name {
    font-family: "Cinzel", "Times New Roman", serif; font-weight: 500;
    font-size: 27px; color: var(--brand-blue); line-height: 1;
  }

  .person-name {
    position: absolute; left: 33px; top: 136px;
    font-family: "Cinzel", "Times New Roman", serif; font-weight: 600; font-size: 31px; line-height: 1;
    color: var(--ink-dark);
  }
  .person-name .first { color: var(--brand-blue); }
  .person-title { position: absolute; left: 33px; top: 172px; font-size: 19px; color: var(--ink); }
  .title-rule { position: absolute; left: 34px; top: 202px; width: 48px; height: 2px; background: var(--brand-blue); }

  .address { position: absolute; left: 31px; top: 248px; font-size: 19px; line-height: 24px; color: var(--ink); }

  .contacts { position: absolute; left: 30px; top: 313px; list-style: none; font-size: 19px; line-height: 24px; color: var(--ink); }
  .contacts li { display: flex; align-items: center; gap: 8px; }
  .contacts svg { width: 15px; height: 15px; fill: var(--brand-blue); flex: none; }
  .contacts .accent { color: var(--brand-blue); }

  .building-art {
    position: absolute; right: 0; top: 0; width: 400px; height: 100%;
    background:
      linear-gradient(90deg, var(--card-light) 0%, rgba(244,244,244,0) 30%),
      linear-gradient(180deg, #c9d6df 0%, #e8e6e2 22%, #9a5a3e 45%, #8b5a43 65%, #8c9a6a 85%, #8a8a88 100%);
  }
</style>
</head>
<body>
  <section class="card card-front" aria-label="Card front">
    <div class="front-mark"></div>
    <div class="front-name">RKW HOLDINGS</div>
  </section>

  <section class="card card-back" aria-label="Card back">
    <div class="building-art" role="img" aria-label="Illustration of a brick and white multi-family apartment building on a tree-lined street"></div>

    <div class="back-brand">
      <span class="mark"></span>
      <span class="name">RKW HOLDINGS</span>
    </div>

    <div class="person-name"><span class="first">MARCUS</span> OLVANE</div>
    <div class="person-title">Director</div>
    <div class="title-rule"></div>

    <div class="address">418, 9th Street<br>Brooklyn NY 11218</div>

    <ul class="contacts">
      <li>
        <svg viewBox="0 0 24 24" aria-hidden="true"><path d="M6.6 10.8a15.1 15.1 0 0 0 6.6 6.6l2.2-2.2c.3-.3.7-.4 1-.2 1.1.4 2.3.6 3.6.6.6 0 1 .4 1 1V20c0 .6-.4 1-1 1A17 17 0 0 1 3 4c0-.6.4-1 1-1h3.5c.6 0 1 .4 1 1 0 1.3.2 2.5.6 3.6.1.3 0 .7-.2 1z"/></svg>
        (917) 482-0657
      </li>
      <li>
        <svg viewBox="0 0 24 24" aria-hidden="true"><path d="M2 5h20v14H2z M3.5 6.5 12 13l8.5-6.5" fill="var(--brand-blue)"/><path d="M3.5 6.5 12 13l8.5-6.5" fill="none" stroke="#fff" stroke-width="1.6"/></svg>
        marcus@rkwholdings-example.com
      </li>
      <li>
        <svg viewBox="0 0 24 24" aria-hidden="true"><circle cx="12" cy="12" r="10"/><path d="M2 12h20M12 2c3 3 3 17 0 20M12 2c-3 3-3 17 0 20" fill="none" stroke="#fff" stroke-width="1.4"/></svg>
        <span>www.<span class="accent">rkwholdings-example</span>.com</span>
      </li>
    </ul>
  </section>
</body>
</html>
```